New singe page website for our software development company

We need a single webpage that includes information about our company, contact details and a job posting. It should scroll vertically with some cool animations and parallax scrolling effects.

We are a software development consulting company that writes custom software for our customers. The webpage should have graphics and illustrations that illustrate this.

Find our logo attached, it can be modified as needed.

Thanks for all the design. When looking through the various design it's clear to us, that car related images does not look right.

We got to have software design/engineering images instead.

Our unique selling points are:

• Custom software development
• Project Managment
• Industry Services
We want these displayed with some text and icons. The icons should either have the red/brown colour from our logo, or a colour that matches the design

Software

```html
<!DOCTYPE html>
<html lang="en">
<head>
<meta charset="utf-8">
<title>Tidewell – Software Development Consulting</title>
<link href="https://fonts.googleapis.com/css2?family=Josefin+Sans:wght@400;600;700&family=Open+Sans:wght@400;600;700&display=swap" rel="stylesheet">
<style>
:root{
  --brand:#7c1d14;
  --accent:#c6504b;
  --ink:#333333;
  --text:#5a5a5a;
  --muted:#777777;
  --sky:#b5d8f2;
  --mist:#eef4f3;
  --field:#d3e0df;
  --footer:#3a3a3a;
  --white:#ffffff;
}
*{margin:0;padding:0;box-sizing:border-box}
html,body{width:1200px;height:2275px;overflow:hidden;background:var(--white)}
body{font-family:"Open Sans",Arial,sans-serif;color:var(--text);position:relative}
.heading{font-family:"Josefin Sans",Arial,sans-serif;font-weight:700;text-transform:uppercase;letter-spacing:1px}

/* header */
.site-header{position:absolute;top:0;left:0;width:1200px;height:83px;background:var(--white);border-bottom:1px solid #e2e2e2}
.brand{position:absolute;left:140px;top:14px;color:var(--brand)}
.brand-name{font-family:"Josefin Sans",sans-serif;font-weight:400;font-size:38px;line-height:38px;color:var(--brand)}
.brand-tag{font-family:"Open Sans",sans-serif;font-size:12px;font-weight:600;color:var(--brand);margin-top:2px}
.main-nav{position:absolute;top:32px;left:594px;display:flex;gap:0}
.main-nav a{font-family:"Josefin Sans",sans-serif;font-weight:600;font-size:17px;color:var(--ink);text-decoration:none;text-transform:uppercase;position:absolute;white-space:nowrap}

/* hero */
.hero{position:absolute;top:83px;left:0;width:1200px;height:547px;overflow:hidden}
.hero-photo{position:absolute;inset:0;background:linear-gradient(90deg,#c9ced4 0%,#e4e7ea 35%,#d7dde3 55%,#a9bfd9 75%,#dfe4ea 100%)}
.hero-copy{position:absolute;left:0;width:1200px;top:180px;text-align:center}
.hero-title{font-family:"Josefin Sans",sans-serif;font-weight:400;font-size:80px;line-height:80px;color:var(--brand)}
.hero-tag{font-family:"Open Sans",sans-serif;font-weight:600;font-size:23px;color:var(--brand);margin-top:2px}
.hero-lead{font-family:"Josefin Sans",sans-serif;font-size:15px;color:var(--ink);text-transform:uppercase;margin-top:10px;letter-spacing:.5px}
.btn{display:inline-block;background:var(--accent);color:var(--white);font-family:"Josefin Sans",sans-serif;font-weight:700;text-transform:uppercase;text-decoration:none;border-radius:3px;text-align:center}
.hero-btn{position:absolute;left:508px;top:344px;width:184px;height:51px;line-height:53px;font-size:18px}

/* about */
.about{position:absolute;top:630px;left:0;width:1200px;height:519px}
.about-title{position:absolute;left:142px;top:62px;font-size:34px;color:var(--accent)}
.about-text{position:absolute;left:142px;top:117px;width:414px;font-size:14px;line-height:22px;color:var(--text)}
.about-text p+p{margin-top:20px}
.devices{position:absolute;left:595px;top:100px;width:453px;height:332px;border-radius:10px;background:linear-gradient(160deg,#3a3a3a 0%,#dfe3e7 40%,#c9ccd0 100%)}

/* services */
.services{position:absolute;top:1149px;left:0;width:1200px;height:349px;background:var(--sky)}
.section-center{position:absolute;top:40px;width:1200px;text-align:center;font-size:28px;color:var(--ink)}
.service{position:absolute;top:114px;width:300px;text-align:center}
.service-icon{width:102px;height:102px;margin:0 auto}
.service-name{font-family:"Open Sans",sans-serif;font-weight:600;font-size:14px;color:var(--ink);text-transform:uppercase;margin-top:22px}
.service-text{font-size:11.5px;line-height:19px;color:var(--text);margin-top:6px}

/* testimonials */
.testimonials{position:absolute;top:1498px;left:0;width:1200px;height:402px}
.section-left{position:absolute;left:140px;top:42px;font-size:28px;color:var(--ink)}
.quote{position:absolute;width:427px}
.quote-text{font-size:12.5px;line-height:20px;color:var(--ink)}
.quote-rule{position:relative;height:6px;margin-top:6px;border-bottom:3px solid #e1e1e1;border-radius:0 0 4px 4px}
.quote-rule svg{position:absolute;left:392px;top:6px}
.quote-name{text-align:right;font-size:13px;font-weight:600;color:var(--ink);margin-top:10px}

/* contact */
.contact{position:absolute;top:1900px;left:0;width:1200px;height:324px;background:var(--mist)}
.contact .section-left{top:50px}
.contact-line{position:absolute;left:145px;display:flex;gap:12px;font-size:13px;line-height:20px;color:var(--ink)}
.contact-line svg{flex:none;margin-top:2px}
.social{position:absolute;left:169px;top:265px;display:flex;gap:10px}
.social span{width:28px;height:28px;background:#a9b9b8}
.field{position:absolute;background:var(--field);font-size:13px;color:#7d8b8a;padding:8px 12px}
.send-btn{position:absolute;left:455px;top:239px;width:110px;height:41px;line-height:43px;font-size:14px}

/* footer */
.site-footer{position:absolute;top:2224px;left:0;width:1200px;height:51px;background:var(--footer);color:var(--white)}
.footer-nav a{position:absolute;top:19px;font-size:11px;font-weight:600;color:var(--white);text-decoration:none;text-transform:uppercase}
.copyright{position:absolute;right:140px;top:19px;font-size:11px}
</style>
</head>
<body>

<header class="site-header">
  <div class="brand">
    <div class="brand-name">Tidewell</div>
    <div class="brand-tag">Software Development Consulting</div>
  </div>
  <nav class="main-nav">
    <a href="#" style="left:0">Home</a>
    <a href="#" style="left:79px">About Us</a>
    <a href="#" style="left:189px">Services</a>
    <a href="#" style="left:293px">Blog</a>
    <a href="#" style="left:367px">Contact Us</a>
  </nav>
</header>

<section class="hero">
  <div class="hero-photo" role="img" aria-label="Photo of a smiling consultant in a shirt and tie in a bright office, with colleagues shaking hands in the background"></div>
  <div class="hero-copy">
    <div class="hero-title">Tidewell</div>
    <div class="hero-tag">Software Development Consulting</div>
    <div class="hero-lead">Lorem ipsum dolor sit amet, consectetur adipisicing elit</div>
  </div>
  <a href="#" class="btn hero-btn">Get Contact</a>
</section>

<section class="about">
  <h2 class="heading about-title">About Tidewell Consulting</h2>
  <div class="about-text">
    <p>Lorem ipsum dolor sit amet, consectetur adipisicing elit, sed do eiusmod tempor incididunt ut labore et dolore magna aliqua. Ut enim ad minim veniam, quis nostrud exercitation ullamco laboris nisi ut aliquip ex ea commodo consequat. Duis aute irure dolor in reprehenderit in voluptate velit esse cillum dolore eu fugiat nulla pariatur. Excepteur sint occaecat cupidatat non proident, sunt in culpa qui officia deserunt mollit anim id est laborum.</p>
    <p>Sed ut perspiciatis unde omnis iste natus error sit voluptatem accusantium doloremque laudantium, totam rem aperiam, eaque ipsa quae ab illo inventore veritatis et quasi architecto beatae vitae dicta sunt explicabo. Nemo enim ipsam voluptatem quia voluptas sit aspernatur aut odit aut fugit, sed quia consequuntur magni dolores eos qui ratione voluptatem sequi nesciunt.</p>
  </div>
  <div class="devices" role="img" aria-label="Illustration of the website shown on a desktop monitor and a tablet"></div>
</section>

<section class="services">
  <h2 class="heading section-center">Our Services</h2>

  <div class="service" style="left:136px">
    <svg class="service-icon" viewBox="0 0 102 102">
      <circle cx="51" cy="51" r="51" fill="var(--accent)"/>
      <rect x="30" y="32" width="42" height="28" rx="2" fill="none" stroke="#fff" stroke-width="4"/>
      <rect x="44" y="60" width="14" height="8" fill="#fff"/>
      <rect x="36" y="68" width="30" height="4" fill="#fff"/>
    </svg>
    <div class="service-name">Custom Software Development</div>
    <div class="service-text">Lorem ipsum dolor sit amet, consectetur adipisicing<br>elit, sed do eiusmod tempor incididunt ut labore et</div>
  </div>

  <div class="service" style="left:451px">
    <svg class="service-icon" viewBox="0 0 102 102">
      <circle cx="51" cy="51" r="51" fill="var(--accent)"/>
      <rect x="30" y="28" width="32" height="40" rx="2" fill="none" stroke="#fff" stroke-width="3"/>
      <rect x="36" y="36" width="20" height="3" fill="#fff"/>
      <rect x="36" y="44" width="20" height="3" fill="#fff"/>
      <rect x="36" y="52" width="12" height="3" fill="#fff"/>
      <circle cx="64" cy="64" r="10" fill="none" stroke="#fff" stroke-width="5" stroke-dasharray="4 3"/>
      <circle cx="64" cy="64" r="4" fill="#fff"/>
    </svg>
    <div class="service-name">Project Managment</div>
    <div class="service-text">Lorem ipsum dolor sit amet, consectetur adipisicing<br>elit, sed do eiusmod tempor incididunt ut labore et</div>
  </div>

  <div class="service" style="left:764px">
    <svg class="service-icon" viewBox="0 0 102 102">
      <circle cx="51" cy="51" r="51" fill="var(--accent)"/>
      <rect x="36" y="26" width="30" height="48" fill="#fff"/>
      <g fill="var(--accent)">
        <rect x="41" y="32" width="6" height="5"/><rect x="55" y="32" width="6" height="5"/>
        <rect x="41" y="42" width="6" height="5"/><rect x="55" y="42" width="6" height="5"/>
        <rect x="41" y="52" width="6" height="5"/><rect x="55" y="52" width="6" height="5"/>
        <rect x="47" y="63" width="8" height="11"/>
      </g>
    </svg>
    <div class="service-name">Industry Services</div>
    <div class="service-text">Lorem ipsum dolor sit amet, consectetur adipisicing<br>elit, sed do eiusmod tempor incididunt ut labore et</div>
  </div>
</section>

<section class="testimonials">
  <h2 class="heading section-left">Testimonials</h2>

  <div class="quote" style="left:140px;top:106px">
    <p class="quote-text">Lorem ipsum dolor sit amet, consectetur adipisicing elit, sed do eiusmod tempor incididunt ut labore et dolore magna aliqua. Ut enim ad minim veniam,quis nostrud exercitation ullamco laboris nisi ut aliquip ex ea commodo consequat</p>
    <div class="quote-rule"><svg width="16" height="9" viewBox="0 0 16 9"><path d="M0 0 L8 8 L16 0" fill="#fff" stroke="#e1e1e1" stroke-width="2"/></svg></div>
    <div class="quote-name">Veltra Partners</div>
  </div>
  <div class="quote" style="left:633px;top:106px">
    <p class="quote-text">Lorem ipsum dolor sit amet, consectetur adipisicing elit, sed do eiusmod tempor incididunt ut labore et dolore magna aliqua. Ut enim ad minim veniam,quis nostrud exercitation ullamco laboris nisi ut aliquip ex ea commodo consequat</p>
    <div class="quote-rule"><svg width="16" height="9" viewBox="0 0 16 9"><path d="M0 0 L8 8 L16 0" fill="#fff" stroke="#e1e1e1" stroke-width="2"/></svg></div>
    <div class="quote-name">R. Halden</div>
  </div>
  <div class="quote" style="left:140px;top:254px">
    <p class="quote-text">Lorem ipsum dolor sit amet, consectetur adipisicing elit, sed do eiusmod tempor incididunt ut labore et dolore magna aliqua. Ut enim ad minim veniam,quis nostrud exercitation ullamco laboris nisi ut aliquip ex ea commodo consequat</p>
    <div class="quote-rule"><svg width="16" height="9" viewBox="0 0 16 9"><path d="M0 0 L8 8 L16 0" fill="#fff" stroke="#e1e1e1" stroke-width="2"/></svg></div>
    <div class="quote-name">R. Halden</div>
  </div>
  <div class="quote" style="left:633px;top:254px">
    <p class="quote-text">Lorem ipsum dolor sit amet, consectetur adipisicing elit, sed do eiusmod tempor incididunt ut labore et dolore magna aliqua. Ut enim ad minim veniam,quis nostrud exercitation ullamco laboris nisi ut aliquip ex ea commodo consequat</p>
    <div class="quote-rule"><svg width="16" height="9" viewBox="0 0 16 9"><path d="M0 0 L8 8 L16 0" fill="#fff" stroke="#e1e1e1" stroke-width="2"/></svg></div>
    <div class="quote-name">Veltra Partners</div>
  </div>
</section>

<section class="contact">
  <h2 class="heading section-left">Contact Us</h2>

  <div class="contact-line" style="top:109px">
    <svg width="16" height="16" viewBox="0 0 16 16"><path d="M3 1 L6 1 L7 5 L5 6.5 C6 9 7 10 9.5 11 L11 9 L15 10 L15 13 C15 14 14 15 13 15 C7 15 1 9 1 3 C1 2 2 1 3 1Z" fill="#9aa8a7"/></svg>
    <span>+1800 555 0142</span>
  </div>
  <div class="contact-line" style="top:142px">
    <svg width="16" height="12" viewBox="0 0 16 12"><rect x="1" y="1" width="14" height="10" fill="none" stroke="#9aa8a7" stroke-width="1.5"/><path d="M1 1 L8 7 L15 1" fill="none" stroke="#9aa8a7" stroke-width="1.5"/></svg>
    <span>info@tidewell.example</span>
  </div>
  <div class="contact-line" style="top:175px">
    <svg width="16" height="22" viewBox="0 0 16 22"><path d="M8 1 C4 1 1 4 1 8 C1 13 8 21 8 21 C8 21 15 13 15 8 C15 4 12 1 8 1Z" fill="#9aa8a7"/><circle cx="8" cy="8" r="3" fill="var(--mist)"/></svg>
    <span>3301 Lorem ipsum dolor sit amet<br>ed ut perspiciatis unde omnis iste natus<br>&nbsp;&nbsp;error sit v</span>
  </div>

  <div class="social"><span></span><span></span><span></span><span></span></div>

  <div class="field" style="left:455px;top:96px;width:290px;height:38px">Name</div>
  <div class="field" style="left:768px;top:96px;width:290px;height:38px">Email</div>
  <div class="field" style="left:455px;top:161px;width:603px;height:59px">Message</div>
  <a href="#" class="btn send-btn">Send</a>
</section>

<footer class="site-footer">
  <nav class="footer-nav">
    <a href="#" style="left:140px">Home</a>
    <a href="#" style="left:194px">About Us</a>
    <a href="#" style="left:273px">Services</a>
    <a href="#" style="left:344px">Blog</a>
    <a href="#" style="left:398px">Contact</a>
  </nav>
  <div class="copyright">© 2014 tidewell consult . All Rights Reserved</div>
</footer>

</body>
</html>
```